Medical clinic VALORECLIN sales materials presentation folder

I am looking for a professional design to a sales/presentation folder for VALORECLIN medical clinic. I would like to get picture of doctor in a class design.
I had an example of a hold marketing and the VALORECLIN LOGO.
VALORECLIN have 5 clinics and we are serious whit lot of doctors. We are doing lot of medical service. I put a doctor picture, but if you have a better choice for the presentation folder don't hesitate to use it.

Target Market(s)

Medical customer and corporation

Industry/Entity Type

Health care

Requirements
Must have
• Professional design - red accent
Nice to have
• Medical doctor picture
Should not have
• Don't want the same hold design that the example

```html
<!DOCTYPE html>
<html lang="en">
<head>
<meta charset="utf-8">
<title>VALORECLIN – Presentation Folder</title>
<link href="https://fonts.googleapis.com/css2?family=Montserrat:wght@700&family=Arimo:wght@400;700&display=swap" rel="stylesheet">
<style>
  :root {
    --backdrop: #6a7171;
    --paper: #f4f4f4;
    --grey-panel: #b9b9b9;
    --red: #c42032;
    --red-light: #d03c4d;
    --red-deep: #a50a1a;
    --ink: #1e1e1e;
    --white: #ffffff;
  }
  html, body {
    margin: 0;
    padding: 0;
    width: 1200px;
    height: 848px;
    overflow: hidden;
    background: var(--backdrop);
  }
  .canvas {
    position: relative;
    width: 1200px;
    height: 848px;
  }
  .folder {
    position: absolute;
    left: 50px;
    top: 54px;
    width: 1100px;
    height: 740px;
    box-shadow: 0 18px 40px rgba(0,0,0,0.35);
  }
  .folder-art {
    position: absolute;
    inset: 0;
    width: 1100px;
    height: 740px;
  }
  .doctor-photo {
    position: absolute;
    left: 300px;
    top: 0;
    width: 440px;
    height: 384px;
    background: linear-gradient(160deg, #e9e9e9 0%, #d8d4d2 55%, #c9c2bf 100%);
  }
  .brand {
    position: absolute;
    left: 720px;
    top: 118px;
    display: flex;
    align-items: center;
    gap: 14px;
  }
  .brand-square {
    width: 30px;
    height: 30px;
    background: var(--red);
  }
  .brand-name {
    font-family: "Montserrat", sans-serif;
    font-weight: 700;
    font-size: 34px;
    letter-spacing: 1px;
    color: var(--ink);
  }
  .contact-line {
    position: absolute;
    left: 330px;
    top: 640px;
    font-family: "Arimo", sans-serif;
    font-size: 12px;
    color: var(--white);
    letter-spacing: 0.4px;
  }
  .contact-line .divider { margin: 0 12px; }
  .contact-line .web { font-weight: 700; }
  .office-address {
    position: absolute;
    left: 150px;
    top: 660px;
    font-family: "Arimo", sans-serif;
    font-size: 10px;
    line-height: 1.45;
    color: var(--white);
    letter-spacing: 0.3px;
  }
  .office-address .office-title { margin-bottom: 6px; }
</style>
</head>
<body>
<main class="canvas">
  <section class="folder">
    <svg class="folder-art" viewBox="0 0 1100 740" xmlns="http://www.w3.org/2000/svg">
      <defs>
        <linearGradient id="pocketLeft" x1="0" y1="0" x2="1" y2="1">
          <stop offset="0" stop-color="var(--red)"/>
          <stop offset="0.4" stop-color="var(--red-light)"/>
          <stop offset="1" stop-color="var(--red)"/>
        </linearGradient>
        <linearGradient id="greyFlap" x1="0" y1="0" x2="1" y2="1">
          <stop offset="0" stop-color="#d2d2d2"/>
          <stop offset="1" stop-color="#a9a9a9"/>
        </linearGradient>
      </defs>
      <!-- paper -->
      <rect class="paper" x="0" y="0" width="1100" height="740" fill="var(--paper)"/>
      <!-- grey side flap -->
      <polygon class="side-flap" points="0,150 230,150 60,740 0,740" fill="url(#greyFlap)"/>
      <!-- top right accent -->
      <polygon class="corner-accent" points="1100,210 1100,370 870,370" fill="var(--red-deep)"/>
    </svg>

    <div class="doctor-photo" role="img" aria-label="Photo of a smiling doctor in a white coat with a stethoscope, writing on a clipboard"></div>

    <svg class="folder-art" viewBox="0 0 1100 740" xmlns="http://www.w3.org/2000/svg">
      <!-- pocket -->
      <polygon class="pocket-left" points="250,384 550,384 550,740 95,740" fill="url(#pocketLeft)"/>
      <polygon class="pocket-right" points="550,384 1100,384 1100,740 550,740" fill="var(--red-deep)"/>
      <line class="fold" x1="550" y1="384" x2="550" y2="740" stroke="rgba(0,0,0,0.12)" stroke-width="1"/>
      <!-- pocket cut-out -->
      <polygon class="pocket-notch" points="730,520 880,540 770,590" fill="#e4e4e4"/>
    </svg>

    <div class="brand">
      <span class="brand-square"></span>
      <span class="brand-name">VALORECLIN</span>
    </div>

    <div class="contact-line">
      <span class="phone">1-800-555-0147</span><span class="divider">|</span><span class="web">www.valoreclin.ca</span>
    </div>

    <address class="office-address">
      <div class="office-title">MONTREAL - HEAD OFFICE</div>
      <div>2450, boul. des Érables, local 210</div>
      <div>Montréal (Québec), H2X 0A0</div>
    </address>
  </section>
</main>
</body>
</html>
```